Pactwise - Training I Consulting I Review - Related to Contracts/Agreements

We provide legal services, we need a plattform to book video online trainings or local trainings classes and appointments (with calendar feature to select date and see availability at screen), payment over internet, legal document creation over webpage, videos will be produces in the next 3 - 4 moths so this is a place holder item. Participants for the Online trainings shall have a login in area with secured password. Appointments for local trainings and Consulting. Consider Outline in file attached. I can send you also a video with more explanation regarding the purpose.

Target Market(s)

Startup/scale up Software companies that intent to have an international business and need help with their contracts, to sell their products. Sales persons.

Industry/Entity Type

Legal

Coding

Coded - Design and coding required

Number of Pages Required

5+ page

Font styles to use
Serif
Sans Serif

Colors
000000
eeeeee
f5f5f5
ffffff
f8fcfd
3277b5
ecf7fb
cadf82
86cfc6

Requirements
Must have
• See file pactwise attached with outline. Moreover see here first starting point: https://moritz-ebbing.sitebuildr-demo.net/mysite-1 . Main inspiration comes from www.advisoryhub-demo.net from the log in area, see the outline in the file attached with the screen shots. At the end I need someone who can draft the full webpage and maintain it for a yearly fee. It must be simple and well structured layout. Lean. 1st landing page shall not scroll, 2 landing page only a little to see the testimonials and foster of page. There should be a Progress Bar to indicate the booking/selection process. Calendar booking. Easy fast booking.
• I like the colour mix, the feeling and the easy structor of:
• https://www.artpitch-demo.net/design/6374387or
• https://www.artpitch-demo.net/design/6372391 or https://www.artpitch-demo.net/design/6374366
• https://www.agencyfind-demo.net/en/web-design/belgium-be
• https://www.artpitch-demo.net/design/5896857
• https://www.artpitch-demo.net/design/5902173
• https://www.artpitch-demo.net/design/17197349
• https://www.artpitch-demo.net/design/5464461
• https://www.artpitch-demo.net/design/7180908
Nice to have
• page for evaluation and interview, see outline attached in the file with screen shots. Document upload.
Should not have
• many pictures, long scroll down pages on the 1st and 2nd ladding pages, many colours and forms. No need for news letter, search field, no need for links to Chatterly and other social media (except workNet).

```html
<!DOCTYPE html>
<html lang="en">
<head>
<meta charset="utf-8">
<title>Pactwise – Services</title>
<link rel="stylesheet" href="https://fonts.googleapis.com/css2?family=Arimo:wght@400&display=swap">
<style>
  :root {
    --ink: #000000;
    --white: #ffffff;
    --muted-text: #6b6b6b;
    --muted-border: #3c3c3c;
    --scene-base: #08090b;
    --scene-warm: #2a1a12;
    --scene-cool: #0e1a2a;
    --scene-grey: #1a1a1c;
  }
  * { box-sizing: border-box; margin: 0; padding: 0; }
  html, body {
    width: 1200px;
    height: 652px;
    overflow: hidden;
    background: var(--ink);
  }
  .landing {
    position: relative;
    width: 1200px;
    height: 652px;
    overflow: hidden;
  }
  .landing__backdrop {
    position: absolute;
    inset: 0;
    background:
      radial-gradient(ellipse 320px 260px at 300px 300px, var(--scene-warm) 0%, transparent 75%),
      radial-gradient(ellipse 300px 240px at 950px 190px, var(--scene-cool) 0%, transparent 75%),
      radial-gradient(ellipse 420px 260px at 760px 500px, var(--scene-grey) 0%, transparent 80%),
      linear-gradient(160deg, #050506 0%, var(--scene-base) 60%, #0a0a0b 100%);
  }
  .service-nav {
    position: absolute;
    left: 321px;
    top: 297px;
    display: flex;
    gap: 10px;
  }
  .service-nav__item {
    width: 179px;
    height: 59px;
    border-radius: 30px;
    border: 1px solid var(--muted-border);
    background: var(--ink);
    color: var(--muted-text);
    font-family: "Arimo", Helvetica, Arial, sans-serif;
    font-size: 13px;
    letter-spacing: 1.6px;
    text-transform: uppercase;
    display: flex;
    align-items: center;
    justify-content: center;
    text-decoration: none;
  }
  .service-nav__item--active {
    border: 1.5px solid var(--white);
    color: var(--white);
  }
</style>
</head>
<body>
  <main class="landing">
    <div class="landing__backdrop" role="img" aria-label="Dimmed photo of hands typing on a laptop showing the Pactwise login screen"></div>
    <nav class="service-nav" aria-label="Services">
      <a class="service-nav__item" href="#training">Training</a>
      <a class="service-nav__item service-nav__item--active" href="#consulting">Consulting</a>
      <a class="service-nav__item" href="#design">Design</a>
    </nav>
  </main>
</body>
</html>
```